Postcard: Live Ever Kinder

Text for front: HOW TO CHANGE THE WORLD IN ONE [note: the word "one" should be underlined] STEPHint: It's up to you...[Note: add arrow or something to indicate "turn over"]Text for back: You're going to spend your entire life with someone you can never get away from. (Guess who?) Wouldn't you rather that person #LiveEverKinder than judgmental or critical? BE the change you want to see! Visit www.LiveEverKinder-hub.com for daily Bright Pebbles and community. PLEASE JOIN US![Note: add logo to left half of back side]Font preference for text: Josefin sans

Target Market(s)

People who would be attracted to Calvera church - unitarian universalist message. It's spiritual without being overtly religious, so the target market is probably early 30s and up but ideally won't turn off Millennials (folks under 30). It should attract attention of people who are open-minded and committed to progressive social change, tired of an atmosphere of hate-mongering and divisiveness.

Requirements
Nice to have
• It would be nice to convey a sense of challenge - there is an idea of "bright pebbles" so something related to fire/sparks is appropriate. This is meant to evoke a deeper, divine love more than a sense of romantic love. This love is more fierce than fluffy! Yet it calls us to be our best selves.
Should not have
• Please avoid excessive pink - just the logo is enough, as this design needs to appeal to men as well as women.

```html
<!DOCTYPE html>
<html lang="en">
<head>
<meta charset="utf-8">
<title>Live Ever Kinder – Postcard</title>
<link rel="stylesheet" href="https://fonts.googleapis.com/css2?family=Josefin+Sans:wght@300;400;600;700&display=swap">
<style>
  :root {
    --pink: #ef88a5;
    --charcoal: #3d3a3a;
    --ink: #111111;
    --paper-light: #fbfbfb;
    --paper-shade: #ebeaea;
    --page: #ffffff;
    --white: #ffffff;
  }
  html, body {
    margin: 0;
    padding: 0;
    width: 1200px;
    height: 1200px;
    overflow: hidden;
    background: var(--page);
    font-family: "Josefin Sans", sans-serif;
  }
  .canvas {
    position: relative;
    width: 1200px;
    height: 1200px;
  }
  .postcard {
    position: absolute;
    left: 264px;
    width: 672px;
    height: 457px;
    overflow: hidden;
    background: linear-gradient(135deg, var(--paper-light) 0%, var(--paper-shade) 55%, var(--paper-light) 100%);
    box-shadow: 0 2px 10px rgba(0,0,0,0.08);
  }
  .postcard--front { top: 88px; }
  .postcard--back { top: 632px; }
  .postcard__bands {
    position: absolute;
    inset: 0;
    width: 100%;
    height: 100%;
  }
  .headline {
    position: absolute;
    left: 0;
    right: 0;
    top: 92px;
    margin: 0;
    text-align: center;
    font-weight: 600;
    font-size: 56px;
    line-height: 59px;
    color: var(--charcoal);
    letter-spacing: -0.5px;
  }
  .headline__accent { color: var(--pink); }
  .headline__underline {
    text-decoration: underline;
    text-decoration-thickness: 3px;
    text-underline-offset: 7px;
  }
  .hint {
    position: absolute;
    left: 189px;
    top: 300px;
    width: 293px;
    height: 51px;
    box-sizing: border-box;
    background: var(--pink);
    border: 3px solid var(--charcoal);
    color: var(--white);
    font-weight: 600;
    font-size: 29px;
    line-height: 50px;
    text-align: center;
  }
  .hint::after {
    content: "";
    position: absolute;
    left: 14px;
    right: 14px;
    bottom: -14px;
    height: 10px;
    border-radius: 50%;
    background: radial-gradient(ellipse at center, rgba(0,0,0,0.25), rgba(0,0,0,0) 70%);
  }
  .brand-mark {
    position: absolute;
    left: 91px;
    top: 70px;
    width: 237px;
    text-align: center;
  }
  .brand-mark__dot {
    display: block;
    width: 120px;
    height: 120px;
    margin: 0 auto 18px;
    border-radius: 50%;
    background: var(--pink);
  }
  .brand-mark__name {
    font-weight: 600;
    font-size: 24px;
    color: var(--charcoal);
  }
  .divider {
    position: absolute;
    left: 348px;
    top: 72px;
    width: 1.5px;
    height: 218px;
    background: var(--charcoal);
  }
  .message {
    position: absolute;
    left: 391px;
    top: 67px;
    width: 240px;
    margin: 0;
    font-weight: 300;
    font-size: 15.5px;
    line-height: 21.4px;
    color: var(--ink);
  }
  .invite {
    position: absolute;
    left: 0;
    right: 0;
    top: 312px;
    margin: 0;
    text-align: center;
    font-weight: 700;
    font-size: 64px;
    line-height: 64px;
    color: var(--ink);
    letter-spacing: -0.5px;
  }
</style>
</head>
<body>
<main class="canvas">

  <section class="postcard postcard--front" aria-label="Postcard front">
    <svg class="postcard__bands" viewBox="0 0 784 533" preserveAspectRatio="none" aria-hidden="true">
      <polygon points="0,0 784,0 784,80 392,42 0,80" fill="var(--pink)"/>
      <polyline points="0,82 392,44 784,82" fill="none" stroke="var(--charcoal)" stroke-width="8"/>
      <polyline points="0,453 392,488 784,453" fill="none" stroke="var(--pink)" stroke-width="6"/>
      <polygon points="0,459 392,494 784,459 784,533 0,533" fill="var(--charcoal)"/>
      <g class="turn-arrow">
        <path d="M698 290 C648 312 632 362 688 376" fill="none" stroke="var(--charcoal)" stroke-width="18" stroke-linecap="round"/>
        <path d="M698 290 C648 312 632 362 688 376" fill="none" stroke="var(--pink)" stroke-width="12" stroke-linecap="round"/>
        <polygon points="682,352 744,376 690,402 698,377" fill="var(--pink)" stroke="var(--charcoal)" stroke-width="3" stroke-linejoin="round"/>
      </g>
    </svg>
    <h1 class="headline">HOW TO CHANGE<br><span class="headline__accent">THE WORLD</span><br>IN <span class="headline__underline">ONE</span> STEP</h1>
    <div class="hint">Hint: It's up to you...</div>
  </section>

  <section class="postcard postcard--back" aria-label="Postcard back">
    <svg class="postcard__bands" viewBox="0 0 784 533" preserveAspectRatio="none" aria-hidden="true">
      <polygon points="0,0 784,0 784,58 392,24 0,58" fill="var(--charcoal)"/>
      <polyline points="0,62 392,28 784,62" fill="none" stroke="var(--pink)" stroke-width="6"/>
      <polyline points="0,455 392,489 784,455" fill="none" stroke="var(--charcoal)" stroke-width="7"/>
      <polygon points="0,460 392,494 784,460 784,533 0,533" fill="var(--pink)"/>
    </svg>
    <div class="brand-mark">
      <span class="brand-mark__dot"></span>
      <span class="brand-mark__name">Live Ever Kinder</span>
    </div>
    <div class="divider"></div>
    <p class="message">You're going to spend your entire life with someone you can never get away from. (Guess who?) Wouldn't you rather that person #LiveEverKinder than judgmental or critical? BE the change you want to see! Visit www.LiveEverKinder-hub.com for daily Bright Pebbles and community.</p>
    <h2 class="invite">PLEASE JOIN US!</h2>
  </section>

</main>
</body>
</html>
```